Book cover for modern/pop-culture-oriented poetry collection

We need a simple, streamlined book-cover design (that'll ultimately be 1600 x 2500 pixels; 300 dpi) for a book of poems. We would like to see three elements on the cover: (1) the title in all caps (GLASSHOURS); (2) the author name in all caps (MIRA VENTO); (3) the main image (attached, slugged "glasshours image"). Image and text should be centered on the cover.

Target Market(s)

Readers of contemporary poetry

Font styles to use
Sans Serif

Requirements
Must have
• Book title, author name, attached photo
Nice to have
• Also attached is the cover of a book (HARBOUR) that is in the style/spirit of what we're looking for.

```html
<!DOCTYPE html>
<html lang="en">
<head>
<meta charset="utf-8">
<title>GLASSHOURS — Mira Vento</title>
<link rel="stylesheet" href="https://fonts.googleapis.com/css2?family=Oswald:wght@600;700&display=swap">
<style>
  :root {
    --stage: #2f3238;
    --cover-light: #d9d9d9;
    --cover-mid: #c6c6c6;
    --cover-shade: #b4b4b4;
    --ink-brown: #6a3112;
    --art-dark: #3b2a1f;
    --art-mid: #6e6a5e;
    --art-light: #9a978a;
  }
  html, body {
    margin: 0;
    padding: 0;
    width: 1200px;
    height: 1200px;
    overflow: hidden;
    background: var(--stage);
  }
  .stage {
    position: relative;
    width: 1200px;
    height: 1200px;
    display: flex;
    align-items: center;
    justify-content: center;
  }
  .book-cover {
    position: relative;
    width: 704px;
    height: 1100px;
    background: radial-gradient(ellipse at 50% 40%, var(--cover-light) 0%, var(--cover-mid) 65%, var(--cover-shade) 100%);
    display: flex;
    flex-direction: column;
    align-items: center;
  }
  .book-title {
    margin: 118px 0 0;
    font-family: "Oswald", "Arial Narrow", sans-serif;
    font-weight: 700;
    font-size: 124px;
    line-height: 1;
    letter-spacing: -1px;
    color: var(--ink-brown);
    text-transform: uppercase;
  }
  .cover-art {
    margin-top: 50px;
    width: 390px;
    height: 600px;
  }
  .cover-art svg {
    display: block;
    width: 100%;
    height: 100%;
  }
  .author-name {
    position: absolute;
    bottom: 88px;
    left: 0;
    right: 0;
    margin: 0;
    text-align: center;
    font-family: "Oswald", "Arial Narrow", sans-serif;
    font-weight: 600;
    font-size: 44px;
    line-height: 1;
    color: var(--ink-brown);
    text-transform: uppercase;
  }
</style>
</head>
<body>
  <main class="stage">
    <article class="book-cover">
      <h1 class="book-title">Glasshours</h1>
      <figure class="cover-art" style="margin-left:0;margin-right:0;margin-bottom:0;">
        <svg viewBox="0 0 390 600" role="img" aria-label="Glasshours image: a vintage wood-cabinet television set with rabbit-ear antennas standing on four tapered legs">
          <defs>
            <radialGradient id="artTone" cx="50%" cy="55%" r="60%">
              <stop offset="0%" stop-color="var(--art-light)"/>
              <stop offset="55%" stop-color="var(--art-mid)"/>
              <stop offset="100%" stop-color="var(--art-dark)"/>
            </radialGradient>
          </defs>
          <rect width="390" height="600" rx="6" fill="url(#artTone)" opacity="0.85"/>
        </svg>
      </figure>
      <p class="author-name">Mira Vento</p>
    </article>
  </main>
</body>
</html>
```